Brimble Diecast Torvel Collectables Website

looking for a vibrant web site marketplace built for diecast car enthusiasts to buy, sell, and trade with ease. Whether you're looking to showcase your own collection or discover rare and exciting models, our site makes the process simple and enjoyable. Clients can browse a curated inventory of high‑quality diecast cars, connect with fellow collectors, and find the perfect pieces to expand their collection. With a smooth user experience and a community-driven spirit, we’re the go‑to destination for anyone passionate about diecast cars.

Target Market(s)

diecast collectors

Industry/Entity Type

Diecast Collectables

Coding

Coded - Design and coding required

Number of Pages Required

3 page

Font styles to use
Sans Serif

Colors
EE7325
F08F49
F5BC92
FAE3D3
FDF4ED

Requirements
Must have
• Cool look and feel. Woo commerce page to post and sell my inventory
Nice to have
• page for users to post their cars or looking for trades.
Should not have
• look cheap

```html
<!DOCTYPE html>
<html lang="en">
<head>
<meta charset="utf-8">
<title>Brimble Diecast — Find Rare Diecast</title>
<link rel="stylesheet" href="https://fonts.googleapis.com/css2?family=Roboto+Slab:wght@800;900&family=Jost:wght@400;500;600&display=swap">
<style>
:root{
  --orange:#ee7325;
  --orange-2:#f08f49;
  --peach:#f5bc92;
  --blush:#fae3d3;
  --cream:#fdf4ed;
  --red:#e4572e;
  --green:#4f6b36;
  --green-dark:#3f5a2b;
  --maroon:#7b2a1f;
  --ink:#1f1a16;
  --muted:#6b5f55;
  --sand:#e6c49c;
  --footer:#2a231d;
  --white:#ffffff;
}
*{box-sizing:border-box;margin:0;padding:0}
html,body{width:1200px;height:5367px;overflow:hidden}
body{font-family:"Jost",sans-serif;color:var(--ink);background:var(--cream);font-size:14px}
.wrap{width:976px;margin:0 auto;position:relative}
h1,h2{font-family:"Roboto Slab",Georgia,serif;font-weight:900;text-transform:uppercase;letter-spacing:.5px;line-height:1.15}
.accent{color:var(--green)}
.accent-o{color:var(--orange)}
.btn{display:inline-flex;align-items:center;gap:14px;height:38px;padding:0 8px 0 14px;border-radius:4px;font-size:14px;font-weight:500;text-decoration:none;box-shadow:3px 3px 0 rgba(0,0,0,.18)}
.btn .ico{width:22px;height:22px;border-radius:50%;display:grid;place-items:center}
.btn-green{background:var(--green);color:var(--white)}
.btn-green .ico{background:var(--white);color:var(--green)}
.btn-white{background:var(--white);color:var(--ink);border:1px solid #ccc}
.btn-white .ico{border:1px solid var(--ink);color:var(--ink)}
.btn-orange{background:var(--red);color:var(--white)}
.btn-orange .ico{background:var(--white);color:var(--red)}
.ph{display:block}

.desert{position:relative;height:1604px;background:linear-gradient(180deg,#d7d2c8 0%,#e4cfb4 30%,#e9c7a0 45%,#e8c59c 100%)}
.topbar{height:32px;background:rgba(255,255,255,.25);font-size:10px;text-align:center;line-height:32px;color:#333}
.topbar span{margin:0 6px}
.nav{position:absolute;top:40px;left:0;right:0;height:80px}
.nav ul{list-style:none;display:flex;gap:24px;position:absolute;top:16px;font-size:14px}
.nav .left{left:114px}
.nav .right{left:714px}
.logo{position:absolute;left:562px;top:6px;width:76px;height:76px;border-radius:50%;background:var(--maroon);display:grid;place-items:center;color:var(--white);font-family:"Jost",sans-serif;font-weight:600;font-size:10px;text-align:center;line-height:1.1}
.nav .cta{position:absolute;left:955px;top:10px;height:32px;font-size:11px}
.hero-car{position:absolute;left:440px;top:180px;width:760px;height:460px;background:radial-gradient(ellipse at 60% 55%,#6d5a44 0%,#9c8466 35%,rgba(220,195,160,0) 70%)}
.hero-copy{position:absolute;left:112px;top:168px}
.hero-copy h1{font-size:50px}
.hero-copy p{margin-top:14px;font-size:14px;width:520px;line-height:1.4}
.hero-copy .actions{margin-top:26px;display:flex;gap:14px}

.explore{position:absolute;top:672px;left:0;right:0}
.sec-head{display:flex;justify-content:space-between;align-items:flex-start}
.sec-head h2{font-size:38px}
.sec-head p{margin-top:8px;font-size:14px;line-height:1.45;max-width:600px}
.cats{display:flex;gap:12px;margin-top:32px}
.cat{width:155px;height:170px;background:var(--white);border-radius:80px 80px 4px 4px;border:1px solid #c9b7a0;overflow:hidden}
.cat .ph{height:124px;border-radius:78px 78px 0 0}
.cat span{display:block;text-align:center;font-size:13px;font-weight:500;padding-top:12px}

.featured{position:absolute;top:1000px;left:0;right:0}
.products{position:absolute;top:120px;left:112px;display:flex;gap:14px;width:1200px}
.prod{width:282px;height:345px;background:var(--white);border-radius:6px;padding:10px;flex:none;box-shadow:0 2px 8px rgba(0,0,0,.08)}
.prod .ph{height:182px;border-radius:4px}
.prod h3{font-size:14px;font-weight:500;margin-top:14px}
.prod .meta{font-size:10px;color:var(--muted);margin-top:8px}
.prod .cond{font-size:10px;color:var(--muted);margin-top:14px;padding-top:8px;border-top:1px solid #e8ddd2}
.prod .price{margin-top:10px;height:36px;border-radius:4px;background:var(--red);color:var(--white);display:flex;justify-content:space-between;align-items:center;padding:0 14px;font-size:14px}
.prod-feature{width:282px;height:345px;border-radius:142px 142px 6px 6px;background:linear-gradient(180deg,#4d5a45,#1d211b);flex:none;position:relative;overflow:hidden}
.prod-feature h3{position:absolute;top:228px;width:100%;text-align:center;color:var(--white);font-weight:500;font-size:20px}
.prod-feature .btn{position:absolute;top:270px;left:76px;box-shadow:none}
.slider{position:absolute;top:1494px;left:112px;width:976px;height:44px}
.track{position:absolute;left:0;top:22px;width:846px;height:2px;background:#c7a883}
.track i{position:absolute;left:0;top:-1px;width:166px;height:4px;background:var(--green)}
.arrows{position:absolute;right:0;top:0;display:flex;gap:12px}
.arrows b{width:42px;height:42px;border:1px solid #8c7760;border-radius:3px;display:grid;place-items:center;background:var(--white)}
.arrows b.on{background:#b4a58a}

.why{height:729px;background:var(--green);position:relative;color:var(--white)}
.why .title{text-align:center;padding-top:60px}
.why h2{font-size:38px}
.why h2 .accent-o{color:var(--peach)}
.why .title p{font-size:14px;opacity:.85;width:720px;margin:14px auto 0;line-height:1.5}
.why-frame{position:absolute;left:48px;top:218px;width:472px;height:272px;border:1px solid var(--orange-2)}
.why-car{position:absolute;left:18px;top:240px;width:540px;height:360px;border-radius:40%;background:radial-gradient(ellipse,#e8e8e8 0%,#b9b9b9 45%,rgba(79,107,54,0) 72%)}
.why-panel{position:absolute;left:562px;top:191px;width:525px;height:470px;background:var(--green-dark);border-radius:6px;padding:28px 34px}
.feat{display:flex;gap:22px;margin-bottom:25px}
.feat .ic{width:62px;height:62px;border-radius:50%;background:var(--white);color:var(--green);display:grid;place-items:center;flex:none}
.feat h4{font-weight:500;font-size:16px}
.feat p{font-size:11.5px;opacity:.75;margin-top:6px;line-height:1.45;width:310px}

.bst{height:584px;background:var(--cream);position:relative}
.bst .title{text-align:center;padding-top:54px}
.bst h2{font-size:38px}
.bst .title p{font-size:14px;color:var(--muted);width:720px;margin:10px auto 0;line-height:1.45}
.bst-cards{position:absolute;top:178px;left:112px;display:flex;gap:20px}
.bcard{width:305px;height:355px;background:var(--white);border-radius:4px;overflow:hidden;box-shadow:0 2px 10px rgba(0,0,0,.06)}
.bcard .ph{height:188px}
.bcard .body{padding:16px 26px}
.bcard h4{font-weight:500;font-size:16px}
.bcard p{font-size:13px;color:var(--muted);margin-top:6px;line-height:1.35;width:240px}
.bcard .btn{margin-top:16px;box-shadow:none}
.bcard.mid{width:325px;border-radius:162px 162px 4px 4px;background:linear-gradient(180deg,#4f7a3b 0%,#2b3b24 100%);color:var(--white);text-align:center;position:relative}
.bcard.mid .body{position:absolute;top:178px;width:100%}
.bcard.mid p{color:var(--white);width:260px;margin:8px auto 0;font-size:12px}
.bcard.mid .btn{margin-top:14px}

.community{height:374px;background:var(--maroon);position:relative;overflow:hidden;color:var(--white)}
.community .copy{position:absolute;left:112px;top:72px}
.community h2{font-size:36px}
.community p{font-size:19px;margin-top:14px;line-height:1.35;width:420px}
.community .btn{margin-top:26px}
.community .ph{position:absolute;left:556px;top:10px;width:720px;height:356px;border-radius:50%;border:4px solid var(--cream);background:radial-gradient(ellipse at 50% 60%,#4a4a4a,#0d0d0d 70%)}

.insights{height:563px;background:var(--cream);position:relative}
.insights .sec-head{padding-top:78px}
.big-post{position:absolute;left:112px;top:184px;width:484px;height:320px;border-radius:6px;overflow:hidden;background:linear-gradient(180deg,#d9d6c6 0%,#8f8a55 45%,#1e1c14 100%);color:var(--white)}
.big-post .tags{position:absolute;top:42px;left:0;display:flex;gap:14px;font-size:11px;align-items:center}
.big-post .tag{background:var(--red);padding:3px 14px}
.big-post .date{color:#f08f49}
.big-post h3{position:absolute;left:30px;top:160px;font-weight:500;font-size:17px}
.big-post p{position:absolute;left:30px;top:190px;width:420px;font-size:12.5px;opacity:.85;line-height:1.35}
.big-post .btn{position:absolute;left:38px;top:258px;box-shadow:none}
.posts{position:absolute;left:620px;top:184px;width:468px}
.post{height:100px;background:var(--white);margin-bottom:11px;display:flex;position:relative;box-shadow:0 1px 6px rgba(0,0,0,.06)}
.post .ph{width:130px;height:100px;flex:none}
.post h4{font-weight:500;font-size:14px;margin:30px 0 0 20px;width:290px;line-height:1.3}
.post small{position:absolute;right:12px;bottom:10px;font-size:11px;color:var(--muted)}
.post .arr{position:absolute;right:12px;top:10px;color:var(--red)}

.reviews{height:594px;background:var(--sand);position:relative}
.reviews .title{text-align:center;padding-top:62px}
.reviews h2{font-size:38px}
.reviews .title p{font-size:14px;margin-top:10px}
.reviews .title .btn{margin-top:20px}
.rev{position:absolute;top:218px;background:var(--white);padding:38px 26px;height:238px;border-radius:3px}
.rev h5{font-weight:400;font-size:14px}
.stars{color:var(--orange);letter-spacing:2px;font-size:13px;margin-top:2px}
.rev p{font-size:12px;color:var(--muted);margin-top:14px;line-height:1.35}
.rev a{display:block;margin-top:24px;font-size:12px;color:var(--red)}
.rev.mid{top:200px;height:256px;padding:16px;display:flex;gap:18px;border-bottom:2px solid var(--red)}
.rev.mid .ph{width:116px;height:206px;flex:none;background:linear-gradient(180deg,#d9cfc2,#8a6c56)}
.rev.mid .txt{padding-top:28px}
.reviews .slider{top:490px}

.cta-sec{height:594px;background:linear-gradient(180deg,var(--cream) 0%,#f4e3d1 35%,#e7c9a7 100%);position:relative;text-align:center}
.cta-sec h2{font-size:40px;padding-top:72px}
.cta-sec p{font-size:19px;margin-top:10px}
.cta-sec .actions{display:flex;gap:16px;justify-content:center;margin-top:26px}
.btn-outline{background:var(--white);color:var(--red);border:1px solid var(--red)}
.btn-outline .ico{background:var(--red);color:var(--white)}
.cta-car{position:absolute;left:262px;top:250px;width:676px;height:300px;border-radius:50%;background:radial-gradient(ellipse,#d7c238 0%,#a89220 35%,rgba(231,201,167,0) 70%)}

.footer{height:325px;background:var(--footer);color:#d9cfc5;position:relative}
.f-brand{position:absolute;left:112px;top:40px}
.f-logo{display:flex;align-items:center;gap:10px;color:var(--white);font-weight:600;font-size:18px}
.f-logo i{width:42px;height:42px;border-radius:50%;background:var(--maroon);display:block}
.f-brand p{margin-top:70px;width:340px;font-size:11.5px;line-height:1.5}
.f-col{position:absolute;top:60px;font-size:12px}
.f-col h6{font-size:13px;font-weight:500;color:var(--white);margin-bottom:16px}
.f-col ul{list-style:none;line-height:1.6;font-size:11px}
.f-links{left:566px}
.f-links ul{columns:2;column-gap:70px}
.f-contact{left:921px}
.f-contact li{display:flex;gap:10px;align-items:center;margin-bottom:16px}
.f-contact .c{width:22px;height:22px;border-radius:50%;border:1px solid #d9cfc5;display:grid;place-items:center}
.f-contact .mail{color:var(--red)}
.vline{position:absolute;top:60px;width:1px;height:150px;background:#5a4f45}
.copy-line{position:absolute;left:112px;right:112px;bottom:0;border-top:1px solid #5a4f45;text-align:center;font-size:11px;padding:14px 0 20px}
</style>
</head>
<body>

<svg width="0" height="0" style="position:absolute">
  <symbol id="arr" viewBox="0 0 12 12"><path d="M3 9 9 3M4 3h5v5" fill="none" stroke="currentColor" stroke-width="1.6"/></symbol>
</svg>

<div class="desert">
  <div class="topbar"><span>Classic</span>|<span>Supercars</span>|<span>JDM</span>|<span>Muscle</span>|<span>Limited</span>|<span>Trucks</span></div>
  <div class="hero-car ph" role="img" aria-label="Off-road diecast truck in desert sand"></div>
  <nav class="nav">
    <ul class="left"><li>Home</li><li>Shop / Browse</li><li>Categories ⌄</li><li>Buy</li><li>Sell</li></ul>
    <div class="logo">Brimble<br>Diecast</div>
    <ul class="right"><li>Trade</li><li>Community</li><li>Blog</li></ul>
    <a class="btn btn-orange cta">Sell Your Car <span class="ico"><svg width="10" height="10"><use href="#arr"/></svg></span></a>
  </nav>
  <div class="hero-copy">
    <h1>Find Rare <span class="accent-o">Diecast.</span><br>Trade With Collectors.</h1>
    <p>A Dedicated Platform Built For Diecast Enthusiasts To Buy, Sell, And Trade Models With Trusted Collectors Around The World.</p>
    <div class="actions">
      <a class="btn btn-green">Browse Collection <span class="ico"><svg width="10" height="10"><use href="#arr"/></svg></span></a>
      <a class="btn btn-white">Start Selling <span class="ico"><svg width="10" height="10"><use href="#arr"/></svg></span></a>
    </div>
  </div>

  <section class="explore">
    <div class="wrap">
      <div class="sec-head">
        <div><h2>Explore By <span class="accent-o">Category</span></h2><p>Find The Models You Love — From Timeless Classics To Rare Collectibles.</p></div>
        <a class="btn btn-green" style="margin-top:18px">View All Categories <span class="ico"><svg width="10" height="10"><use href="#arr"/></svg></span></a>
      </div>
      <div class="cats">
        <div class="cat"><div class="ph" role="img" aria-label="Red classic diecast car" style="background:linear-gradient(160deg,#f1e8e2,#c23a2c)"></div><span>Classic Cars</span></div>
        <div class="cat"><div class="ph" role="img" aria-label="Orange supercar model" style="background:linear-gradient(160deg,#dfe9f0,#e06a2b)"></div><span>Supercars</span></div>
        <div class="cat"><div class="ph" role="img" aria-label="Red JDM model car" style="background:linear-gradient(160deg,#2f7d80,#d43b2a)"></div><span>JDM Legends</span></div>
        <div class="cat"><div class="ph" role="img" aria-label="Red muscle car on grass" style="background:linear-gradient(160deg,#a7c27d,#b0322a)"></div><span>Muscle Cars</span></div>
        <div class="cat"><div class="ph" role="img" aria-label="Rows of colourful limited edition models" style="background:linear-gradient(160deg,#e6473a,#f0c23a,#3a6ec2)"></div><span>Limited Editions</span></div>
        <div class="cat"><div class="ph" role="img" aria-label="Red utility truck model" style="background:linear-gradient(160deg,#1a1a1a,#b8271f)"></div><span>Trucks &amp; Utility</span></div>
      </div>
    </div>
  </section>

  <section class="featured">
    <div class="wrap">
      <div class="sec-head">
        <div><h2>Featured <span class="accent">Diecast Models</span></h2><p>Explore Handpicked Diecast Cars Trending Among Collectors Right Now — From Rare Vintage Finds To Limited-Edition Masterpieces Ready To Elevate Your Collection.</p></div>
        <a class="btn btn-green" style="margin-top:28px">View All Products <span class="ico"><svg width="10" height="10"><use href="#arr"/></svg></span></a>
      </div>
    </div>
    <div class="products">
      <div class="prod"><div class="ph" role="img" aria-label="Yellow supercar model on white" style="background:linear-gradient(180deg,#f6f1ea,#e3a22b 70%,#f6f1ea)"></div>
        <h3>Vellano Rossa Signature Edition</h3><div class="meta">Scale: 1:18 &nbsp;|&nbsp; Brand: Bravollo &nbsp;|&nbsp; Year: 2015</div>
        <div class="cond">Condition: &nbsp;Like New (Display Case Kept)</div><div class="price"><span>Price :</span><span>$129.00</span></div></div>
      <div class="prod-feature" role="img" aria-label="Racing livery model car close-up"><h3>Kaito Strada RS</h3><a class="btn btn-orange">Shop Now</a></div>
      <div class="prod"><div class="ph" role="img" aria-label="Red classic fastback model" style="background:linear-gradient(180deg,#bfe3ef,#d83a2b 70%,#e9f3f6)"></div>
        <h3>1967 Halden Stallion Fastback</h3><div class="meta">Scale: 1:18 &nbsp;|&nbsp; Brand: Maxeon &nbsp;|&nbsp; Year: 1967</div>
        <div class="cond">Condition: &nbsp;Like New (Display Case Kept)</div><div class="price"><span>Price :</span><span>$75.00</span></div></div>
      <div class="prod"><div class="ph" role="img" aria-label="White supercar model on dark" style="background:linear-gradient(180deg,#2a2a2a,#cfcfcf 70%,#2a2a2a)"></div>
        <h3>Corvano Lucera S</h3><div class="meta">Scale: 1:18 &nbsp;|&nbsp; Brand: ArtoCraft</div>
        <div class="cond">Condition: &nbsp;Mint (Unopened Box)</div><div class="price"><span>Price :</span><span></span></div></div>
    </div>
  </section>
  <div class="slider">
    <div class="track"><i></i></div>
    <div class="arrows"><b class="on">←</b><b>→</b></div>
  </div>
</div>

<section class="why">
  <div class="title">
    <h2>Why Collectors <span class="accent-o">Choose</span> Us</h2>
    <p>Built For Enthusiasts, Trusted By Collectors — We Provide A Secure, Seamless, And Community-Driven Marketplace Where Every Transaction Feels Confident And Every Connection Matters.</p>
  </div>
  <div class="why-frame"></div>
  <div class="why-car ph" role="img" aria-label="White hypercar model"></div>
  <div class="why-panel">
    <div class="feat"><div class="ic"><svg width="28" height="28" viewBox="0 0 24 24" fill="none" stroke="currentColor" stroke-width="1.6"><path d="M12 3 4 6v6c0 5 4 8 8 9 4-1 8-4 8-9V6z"/><path d="m8.5 12 2.5 2.5 4.5-5"/></svg></div><div><h4>Verified Listings</h4><p>Every Car Is Carefully Reviewed To Ensure Authenticity, Quality, And Accurate Representation.</p></div></div>
    <div class="feat"><div class="ic"><svg width="28" height="28" viewBox="0 0 24 24" fill="none" stroke="currentColor" stroke-width="1.6"><rect x="3" y="6" width="18" height="12" rx="2"/><path d="M3 10h18"/></svg></div><div><h4>Secure Transactions</h4><p>Enjoy Safe Payments And Protected Trades With A System Designed To Keep Collectors Worry-Free.</p></div></div>
    <div class="feat"><div class="ic"><svg width="28" height="28" viewBox="0 0 24 24" fill="none" stroke="currentColor" stroke-width="1.6"><circle cx="12" cy="12" r="9"/><path d="M3 12h18M12 3c3 3 3 15 0 18M12 3c-3 3-3 15 0 18"/></svg></div><div><h4>Global Community</h4><p>Connect With Passionate Collectors From Around The World And Expand Your Network.</p></div></div>
    <div class="feat"><div class="ic"><svg width="28" height="28" viewBox="0 0 24 24" fill="none" stroke="currentColor" stroke-width="1.6"><rect x="4" y="4" width="16" height="16" rx="3"/><path d="M8 9h8M8 13h8M8 17h4"/></svg></div><div><h4>Easy Listing Tools</h4><p>Create Listings In Minutes With Simple Tools Designed For Speed And Convenience.</p></div></div>
    <div class="feat"><div class="ic"><svg width="28" height="28" viewBox="0 0 24 24" fill="none" stroke="currentColor" stroke-width="1.6"><path d="M4 12a8 8 0 1 1 4 7l-4 1 1-4a8 8 0 0 1-1-4z"/></svg></div><div><h4>Built-In Messaging</h4><p>Communicate Directly With Buyers And Sellers To Negotiate, Ask Questions, And Trade Easily.</p></div></div>
  </div>
</section>

<section class="bst">
  <div class="title">
    <h2>Buy. Sell. Trade — All In One Place</h2>
    <p>Whether You're Searching For Rare Finds, Selling Your Collection, Or Trading With Fellow Enthusiasts, Our Platform Makes Every Step Simple, Secure, And Built For Collectors.</p>
  </div>
  <div class="bst-cards">
    <div class="bcard"><div class="ph" role="img" aria-label="Racing stock car model" style="background:linear-gradient(160deg,#3a3a3a,#d8b23a,#2a2a2a)"></div>
      <div class="body"><h4>BUY</h4><p>Explore A Wide Range Of Diecast Cars From Verified Collectors Around The World.</p><a class="btn btn-green">Browse Listings <span class="ico"><svg width="10" height="10"><use href="#arr"/></svg></span></a></div></div>
    <div class="bcard mid" role="img" aria-label="Green racing model car">
      <div class="body"><h4>SELL</h4><p>Create Listings In Minutes<br>Upload Multiple Photos For Better Visibility<br>Reach A Global Audience Of Collectors<br>Track Views, Offers, And Sales In Real Time</p><a class="btn btn-orange">Start Selling <span class="ico"><svg width="10" height="10"><use href="#arr"/></svg></span></a></div></div>
    <div class="bcard"><div class="ph" role="img" aria-label="Blue classic race car models" style="background:linear-gradient(160deg,#0f2747,#2f6db0,#0f2747)"></div>
      <div class="body"><h4>TRADE</h4><p>Exchange Models With Other Collectors In A Safe And Structured Way.</p><a class="btn btn-green">Explore Trades <span class="ico"><svg width="10" height="10"><use href="#arr"/></svg></span></a></div></div>
  </div>
</section>

<section class="community">
  <div class="copy">
    <h2>Join The Collector<br>Community</h2>
    <p>Share Your Collection, Discover Rare Finds, And Connect With Passionate Enthusiasts.</p>
    <a class="btn btn-white">Join The Community <span class="ico"><svg width="10" height="10"><use href="#arr"/></svg></span></a>
  </div>
  <div class="ph" role="img" aria-label="Row of colourful sports car models on a dark floor"></div>
</section>

<section class="insights">
  <div class="wrap sec-head">
    <div><h2>Collector Insights &amp; Guides</h2><p>Tips, Guides, And Insights To Help You Discover Rare Models, Grow Your Collection, And Become A Smarter Diecast Collector.</p></div>
    <a class="btn btn-green" style="margin-top:26px">View All Products <span class="ico"><svg width="10" height="10"><use href="#arr"/></svg></span></a>
  </div>
  <article class="big-post" role="img" aria-label="Yellow classic car model with open hood">
    <div class="tags"><span class="tag">Collecting</span><span class="date">Mar 10, 2026 &nbsp;|&nbsp; 5 Min Read</span></div>
    <h3>Top 10 Rare Diecast Cars Every Collector Wants</h3>
    <p>Discover The Most Sought-After Diecast Models That Every Serious Collector Dreams Of Owning — From Limited Editions To Discontinued Classics.</p>
    <a class="btn btn-green">Read More <span class="ico"><svg width="10" height="10"><use href="#arr"/></svg></span></a>
  </article>
  <div class="posts">
    <div class="post"><div class="ph" role="img" aria-label="Boxed diecast cars on shelf" style="background:linear-gradient(160deg,#e0b33a,#6b4a2a)"></div><h4>Beginner's Guide To Starting A Diecast Collection</h4><svg class="arr" width="12" height="12"><use href="#arr"/></svg><small>Mar 05, 2026 &nbsp;|&nbsp; 6 Min Read</small></div>
    <div class="post"><div class="ph" role="img" aria-label="Red racing car models" style="background:linear-gradient(160deg,#c8241c,#2a0f0c)"></div><h4>How To Spot Authentic Vs. Replica Diecast Models</h4><svg class="arr" width="12" height="12"><use href="#arr"/></svg><small>Feb 28, 2026 &nbsp;|&nbsp; 4 Min Read</small></div>
    <div class="post"><div class="ph" role="img" aria-label="Yellow model car display" style="background:linear-gradient(160deg,#e6c72b,#2a2a1a)"></div><h4>How To Properly Store And Display Your Diecast Cars</h4><svg class="arr" width="12" height="12"><use href="#arr"/></svg><small>Feb 20, 2026 &nbsp;|&nbsp; 5 Min Read</small></div>
  </div>
</section>

<section class="reviews">
  <div class="title">
    <h2>What Collectors Are Saying</h2>
    <p>Real Experiences From Collectors Who Buy, Sell, And Trade On Our Platform Every Day.</p>
    <a class="btn btn-green">Join Thousands Of Happy Collectors <span class="ico"><svg width="10" height="10"><use href="#arr"/></svg></span></a>
  </div>
  <div class="rev" style="left:112px;width:292px"><h5>— James L., Seller</h5><div class="stars">★★★★★</div><p>"Selling My Collection Was Fast, Easy, And Completely Stress-Free. I Listed My Cars In Minutes And Started Getting Offers Almost Instantly."</p><a>Sold 25+ Models</a></div>
  <div class="rev mid" style="left:429px;width:337px"><div class="ph" role="img" aria-label="Portrait of a collector holding a model car"></div><div class="txt"><h5>— Alex R., Collector</h5><div class="stars">★★★★★</div><p>"Found Rare Models I've Been Searching For Years. The Trading System Is A Game Changer — Smooth, Reliable, And Actually Fun To Use."</p></div></div>
  <div class="rev" style="left:792px;width:296px"><h5>— Priya S., Collector</h5><div class="stars">★★★★★</div><p>"The Community Here Is Amazing. I've Connected With Collectors From Different Countries And Even Completed Trades I Never Thought Possible."</p><a>Active Trader</a></div>
  <div class="slider"><div class="track"><i style="width:220px"></i></div><div class="arrows"><b class="on">←</b><b>→</b></div></div>
</section>

<section class="cta-sec">
  <h2>Ready To Grow Your Collection?</h2>
  <p>Join Thousands Of Collectors Buying, Selling, And Trading Every Day.</p>
  <div class="actions">
    <a class="btn btn-green">Start Browsing <span class="ico"><svg width="10" height="10"><use href="#arr"/></svg></span></a>
    <a class="btn btn-outline">Start Browsing <span class="ico"><svg width="10" height="10"><use href="#arr"/></svg></span></a>
  </div>
  <div class="cta-car ph" role="img" aria-label="Yellow muscle car model"></div>
</section>

<footer class="footer">
  <div class="f-brand">
    <div class="f-logo"><i></i>Brimble Diecast</div>
    <p>We Are A Global Marketplace Built For Diecast Enthusiasts To Buy, Sell, And Trade Models With Ease. Our Platform Connects Collectors, Simplifies Transactions, And Helps You Discover Rare Pieces From Around The World.</p>
  </div>
  <div class="vline" style="left:496px"></div>
  <div class="f-col f-links"><h6>Quick Links :</h6><ul><li>Home</li><li>Shop / Browse</li><li>Categories</li><li>Buy</li><li>Sell</li><li>Trade</li><li>Community</li><li>Blog</li></ul></div>
  <div class="vline" style="left:876px"></div>
  <div class="f-col f-contact"><h6>Contact Us</h6><ul>
    <li><span class="c"><svg width="11" height="11" viewBox="0 0 24 24" fill="currentColor"><path d="M6 2h4l2 5-3 2c1 3 3 5 6 6l2-3 5 2v4c0 1-1 2-2 2C10 20 4 14 4 4c0-1 1-2 2-2z"/></svg></span>+1 555-014-2290</li>
    <li><span class="c"><svg width="11" height="11" viewBox="0 0 24 24" fill="none" stroke="currentColor" stroke-width="2"><rect x="3" y="5" width="18" height="14"/><path d="m3 6 9 7 9-7"/></svg></span><span class="mail">support@brimblediecast.com</span></li>
  </ul></div>
  <div class="copy-line">© 2026 Brimble Diecast.Com — All Rights Reserved</div>
</footer>

</body>
</html>
```